Flyer Design & Business Cards

I have tried to make up some flyer and have attached them as info with what we would like included. I would like them made to look more professional and I would like business cards along the same line.

Industry/Entity Type

Business

```html
<!DOCTYPE html>
<html lang="en">
<head>
<meta charset="utf-8">
<title>Eastbay Inn – Business Cards</title>
<link rel="stylesheet" href="https://fonts.googleapis.com/css2?family=Montserrat:wght@500;800&family=Special+Elite&display=swap">
<style>
  :root {
    --page-bg: #e9e7e4;
    --front-top: #244a66;
    --front-mid: #163247;
    --front-bottom: #1d1214;
    --ribbon: #f2ac3a;
    --name-ink: #15324a;
    --white: #ffffff;
    --back-blue: #045a80;
    --dot-light: #1da1e0;
    --dot-dark: #2a5a9a;
  }
  * { box-sizing: border-box; margin: 0; padding: 0; }
  html, body { width: 1200px; height: 775px; overflow: hidden; }
  body {
    background: var(--page-bg);
    position: relative;
    font-family: "Montserrat", Arial, sans-serif;
  }
  .card {
    position: absolute;
    top: 107px;
    width: 320px;
    height: 560px;
    border-radius: 4px;
    overflow: hidden;
    box-shadow: 0 6px 18px rgba(0,0,0,0.18);
  }
  .card--front {
    left: 230px;
    background:
      radial-gradient(ellipse 70% 45% at 50% 40%, rgba(60,110,150,0.55), transparent 70%),
      linear-gradient(180deg, var(--front-top) 0%, var(--front-mid) 55%, var(--front-bottom) 100%);
  }
  .card--back {
    left: 650px;
    background: var(--back-blue);
  }
  .ribbon { position: absolute; left: 0; top: 0; }
  .brand-name {
    position: absolute;
    top: 120px;
    left: 0;
    width: 100%;
    text-align: center;
    font-weight: 800;
    font-size: 28px;
    line-height: 1.15;
    color: var(--name-ink);
  }
  .phone {
    position: absolute;
    top: 372px;
    width: 100%;
    text-align: center;
    font-weight: 800;
    font-size: 38px;
    letter-spacing: -0.5px;
    color: var(--white);
  }
  .address {
    position: absolute;
    top: 422px;
    width: 100%;
    text-align: center;
    font-weight: 500;
    font-size: 12px;
    color: var(--white);
  }
  .social {
    position: absolute;
    top: 456px;
    width: 100%;
    display: flex;
    justify-content: center;
    gap: 6px;
  }
  .social-dot { width: 38px; height: 38px; border-radius: 50%; }
  .social-dot--light { background: var(--dot-light); }
  .social-dot--dark { background: var(--dot-dark); }
  .services {
    position: absolute;
    top: 150px;
    width: 100%;
    text-align: center;
    font-family: "Special Elite", "Courier New", monospace;
    font-size: 26px;
    color: var(--white);
    list-style: none;
  }
  .services li { line-height: 1; }
  .services .star { font-size: 26px; margin: 20px 0; }
</style>
</head>
<body>
  <section class="card card--front" aria-label="Business card front">
    <svg class="ribbon" width="320" height="560" viewBox="0 0 320 560">
      <polygon points="85,0 235,0 235,310 160,270 85,310" fill="var(--ribbon)"/>
    </svg>
    <div class="brand-name">Eastbay<br>Inn</div>
    <div class="phone">01632 960418</div>
    <div class="address">Harbour Road, Isle of Carrow HS9 2QT</div>
    <div class="social">
      <span class="social-dot social-dot--light"></span>
      <span class="social-dot social-dot--dark"></span>
    </div>
  </section>

  <section class="card card--back" aria-label="Business card back">
    <ul class="services">
      <li>Real Ales</li>
      <li class="star">★</li>
      <li>Bar Food</li>
      <li class="star">★</li>
      <li>Live Music</li>
    </ul>
  </section>
</body>
</html>
```